Online-Marketing Material für Recruiting-Plattform
Zielgruppe
Recruiting-Plattform für Physiotherapeuten. Wir sind Vermittler.
Aufgabenstellung
Ich benötige ein 2er Set aus Social-Media-Templates, das wir als Basis für Recruiting-Ads nutzen können.
Variante 1: (1080 x 1350) mit jeweils 285 Pixel Safe Space oben und unten (hier keine wichtigen Elemente).
Wichtig: Es handelt sich um ein Template. Daher muss es mit verschiedenen Elementen und Fotos funktionieren.
Die Elemente werden später durch variable Inhalte gesetzt. Ziel ist es, ein möglichst flexibles Format zu schaffen,
das mit unterschiedlichen Inhalten funktioniert.
Bitte orientiere dich am Grunddesign der Website therapunkt.de
Elemente und zugehörige Beispiele sind
1. Foto in querformat | Beispiel als Download)
2. Jobtitel als Headline | (Physiotherapeut (m/w/d)
3. Subtitle | Werde Teil eines wachsenden Teams
4. Arbeitszeitmodell | Vollzeit, Teilzeit
3. Ort | Hannover
4. 3 x Highlights | 1. Betriebliche Krankenversicherung 2. Tretlux 3. Gehalt bis zu 4.500 EUR
(Die Highlight variieren thematisch, daher hier bitte nur mit thematisch-neutralen Icons arbeiten.
5. Logo des Arbeitgebers (lusen) auf weiß
Variante 2 mit Foto in hochformat

```html
<!DOCTYPE html>
<html lang="de">
<head>
<meta charset="utf-8">
<title>Recruiting-Templates Physiotherapeut</title>
<link href="https://fonts.googleapis.com/css2?family=Mulish:ital,wght@0,500;0,600;0,800;0,900;1,800&display=swap" rel="stylesheet">
<style>
  :root {
    --stage: #e7e7e7;
    --white: #ffffff;
    --pink: #fd5585;
    --pink-deep: #f25583;
    --blue: #0293c9;
    --ink: #111111;
    --photo-cool-a: #dfe9ee;
    --photo-cool-b: #9fb7c4;
    --photo-warm-a: #fbeed3;
    --photo-warm-b: #8f8a80;
  }
  * { box-sizing: border-box; margin: 0; padding: 0; }
  html, body {
    width: 1200px; height: 960px; overflow: hidden;
    background: var(--stage);
    font-family: "Mulish", "Nunito Sans", sans-serif;
    color: var(--ink);
  }
  .template {
    position: absolute; top: 161px;
    width: 510px; height: 638px;
    background: var(--white); overflow: hidden;
  }
  .template--landscape { left: 65px; }
  .template--portrait { left: 624px; }
  .backdrop { position: absolute; inset: 0; width: 510px; height: 638px; }
  .abs { position: absolute; white-space: nowrap; }
  .job-gender { font-size: 12.5px; font-weight: 600; }
  .job-title { font-size: 33px; font-weight: 900; letter-spacing: -0.2px; line-height: 1; }
  .job-location { font-size: 17px; font-weight: 900; }
  .employer {
    display: flex; align-items: center; gap: 6px;
    color: var(--white); font-size: 23px; font-weight: 600; letter-spacing: 0.5px;
  }
  .employer-dot { width: 14px; height: 14px; border-radius: 50%; background: var(--white); }
  .subtitle {
    color: var(--pink); font-size: 18px; font-weight: 800; font-style: italic; line-height: 21px;
  }
  .highlight { font-size: 16.5px; font-weight: 500; line-height: 20.5px; }
  .highlight-icon { position: absolute; width: 16px; height: 16px; }
  .work-model { color: var(--white); font-size: 15px; font-weight: 800; font-style: italic; }
  .photo-frame {
    position: absolute; background: var(--white);
    border-radius: 18px; padding: 5px;
    box-shadow: 0 6px 18px rgba(0,0,0,0.12);
  }
  .photo { width: 100%; height: 100%; border-radius: 13px; }
  .photo--treatment { background: linear-gradient(120deg, var(--photo-cool-a) 0%, #eef2f3 45%, var(--photo-cool-b) 100%); }
  .photo--room { background: linear-gradient(160deg, var(--photo-warm-a) 0%, #f4f1ea 50%, var(--photo-warm-b) 100%); }
</style>
</head>
<body>

<svg width="0" height="0" style="position:absolute">
  <defs>
    <symbol id="icon-care" viewBox="0 0 16 16">
      <path d="M8 14.5 1.8 8.4C.2 6.8.4 4 2.3 2.8 3.9 1.8 5.9 2.2 7 3.6L8 4.8l1-1.2c1.1-1.4 3.1-1.8 4.7-.8 1.9 1.2 2.1 4 .5 5.6Z" fill="#fd5585"/>
      <circle cx="11.6" cy="11" r="3.6" fill="#ffffff"/>
      <circle cx="11.6" cy="11" r="2.8" fill="#fd5585"/>
      <path d="m10.2 11 1 1 1.7-1.8" stroke="#ffffff" stroke-width="1" fill="none"/>
    </symbol>
    <symbol id="icon-case" viewBox="0 0 16 16">
      <path d="M5.5 4V2.8c0-.5.4-.8.8-.8h3.4c.4 0 .8.3.8.8V4" stroke="#fd5585" stroke-width="1.4" fill="none"/>
      <rect x="1" y="4" width="14" height="10" rx="1.6" fill="#fd5585"/>
      <rect x="1" y="8" width="14" height="1.2" fill="#ffffff"/>
    </symbol>
    <symbol id="icon-money" viewBox="0 0 16 16">
      <path d="M5.5 1.5h5L9.3 4.2H6.7Z" fill="#fd5585"/>
      <path d="M6.5 4.8h3C12.3 6.6 14 9.5 14 11.8 14 14 12.4 15 8 15s-6-1-6-3.2C2 9.5 3.7 6.6 6.5 4.8Z" fill="#fd5585"/>
      <path d="M9.6 9.3a1.9 1.9 0 1 0 0 3M6.3 10.3h2.6M6.3 11.3h2.6" stroke="#ffffff" stroke-width=".9" fill="none"/>
    </symbol>
  </defs>
</svg>

<!-- Variante 1: Querformat -->
<section class="template template--landscape">
  <svg class="backdrop" viewBox="0 0 510 638" aria-hidden="true">
    <path d="M0 0H510V196Q490 206 470 212Q458 216 440 212L0 103Z" fill="var(--pink)"/>
    <path d="M0 481Q70 440 290 447L510 470V638H0Z" fill="var(--blue)"/>
  </svg>

  <div class="abs job-gender" style="left:38px; top:154px;">(m/w/d)</div>
  <div class="abs job-title" style="left:37px; top:178px;">Physiotherapeut</div>
  <div class="abs job-location" style="left:38px; top:213px;">in Hannover</div>

  <div class="abs employer" style="left:384px; top:153px;"><span>lusen</span><span class="employer-dot"></span></div>

  <div class="photo-frame" style="left:25px; top:249px; width:257px; height:218px;">
    <div class="photo photo--treatment" role="img" aria-label="Foto im Querformat: Physiotherapeutin behandelt einen Patienten auf der Liege"></div>
  </div>

  <div class="abs subtitle" style="left:304px; top:263px;">Werde Teil eines<br>wachsenden Teams</div>

  <svg class="highlight-icon" style="left:304px; top:316px;"><use href="#icon-care"/></svg>
  <div class="abs highlight" style="left:327px; top:313px;">Betriebliche<br>Krankenversicherung</div>

  <svg class="highlight-icon" style="left:304px; top:367px;"><use href="#icon-case"/></svg>
  <div class="abs highlight" style="left:327px; top:364px;">Tretlux</div>

  <svg class="highlight-icon" style="left:304px; top:397px;"><use href="#icon-money"/></svg>
  <div class="abs highlight" style="left:327px; top:394px;">Gehalt bis zu<br>4.500 EUR</div>

  <div class="abs work-model" style="left:312px; top:467px;">Vollzeit, Teilzeit</div>
</section>

<!-- Variante 2: Hochformat -->
<section class="template template--portrait">
  <svg class="backdrop" viewBox="0 0 510 638" aria-hidden="true">
    <path d="M105 0H510V212L366 210Z" fill="var(--pink-deep)"/>
    <path d="M0 490C40 462 70 451 100 451C130 451 150 460 170 472L430 638H0Z" fill="var(--blue)"/>
  </svg>

  <div class="abs job-gender" style="left:37px; top:154px;">(m/w/d)</div>
  <div class="abs job-title" style="left:36px; top:178px;">Physiotherapeut</div>
  <div class="abs job-location" style="left:37px; top:213px;">in Hannover</div>

  <div class="abs employer" style="left:369px; top:156px;"><span>lusen</span><span class="employer-dot"></span></div>

  <div class="photo-frame" style="left:269px; top:210px; width:224px; height:300px;">
    <div class="photo photo--room" role="img" aria-label="Foto im Hochformat: heller Behandlungsraum mit Therapieliege"></div>
  </div>

  <div class="abs subtitle" style="left:36px; top:253px;">Werde Teil eines<br>wachsenden Teams</div>

  <svg class="highlight-icon" style="left:32px; top:318px;"><use href="#icon-care"/></svg>
  <div class="abs highlight" style="left:54px; top:315px;">Betriebliche<br>Krankenversicherung</div>

  <svg class="highlight-icon" style="left:32px; top:368px;"><use href="#icon-case"/></svg>
  <div class="abs highlight" style="left:54px; top:365px;">Tretlux</div>

  <svg class="highlight-icon" style="left:32px; top:398px;"><use href="#icon-money"/></svg>
  <div class="abs highlight" style="left:54px; top:395px;">Gehalt bis zu 4.500 EUR</div>

  <div class="abs work-model" style="left:41px; top:470px;">Vollzeit, Teilzeit</div>
</section>

</body>
</html>
```